Redesign screen for Savings Mobile App

We need a resign of our whole app. This time, we are offering the redesign of one of the screens to see all your potential. Our intention later is to do the whole app, plus corporate web site, brochures, business cards, etc. So yes there is more to work on in the near future.
Let me share some details about what the app does and is it about:
-Focused on customer fidelity to small and medium businesses.
-The app lets the customers win free samples, discounts, gifts on the store that they like. Money savings basically.
-It will be mostly used by young users (female and male) around 18 to 40 years old.
-The app focus on get free discounts, gifts as free coffees, ice-creams, etc.
-Will use a lot of pinwharf in terms of announcements, sharing and more.

So the design should look fresh and funny. This is an hybrid html5/css3 android app. Our focus is now Android so please make sure to follow http://www.zorvelo.com/design/

The attached screenshot is a sample of the working app that we have now. Notice that it lacks of design, it is basically just a raw design of the controls that we needed in place. That is why we need your creativity.

Here we are looking for basically 2 new redesigns:
1 - The screen per se.
2 - The fortune wheel. I attached a screenshot of one that I like. Of course it should not be the same but follow the same idea.

Industry/Entity Type

Store

Font styles to use
Other font styles liked:
• Signika

Requirements
Must have
• Fresh and Funny design
Should not have
• Dark and negative colors

```html
<!DOCTYPE html>
<html lang="es">
<head>
<meta charset="utf-8">
<title>A Jugar – Ruleta</title>
<link rel="stylesheet" href="https://fonts.googleapis.com/css2?family=Lora:wght@400;500&family=Roboto:wght@400;500&display=swap">
<style>
  :root {
    --stage: #1b3f6e;
    --screen-top: #6f5fe6;
    --screen-mid: #3f78cf;
    --screen-bottom: #137a9e;
    --appbar: #7a6ff0;
    --statusbar: #101418;
    --navbar: #050608;
    --text: #ffffff;
    --brand: #8ee7ff;
    --wheel-ring: #1f5f86;
    --wheel-seg: #2a7aa3;
    --wheel-line: #6fb3d3;
    --hub: #ffffff;
    --pointer: #0e3550;
    --button: #0e2f4a;
  }
  * { box-sizing: border-box; margin: 0; padding: 0; }
  html, body { width: 1200px; height: 900px; overflow: hidden; }
  body {
    background: var(--stage);
    display: flex; align-items: center; justify-content: center;
    font-family: "Lora", Georgia, serif;
    color: var(--text);
  }
  .screen {
    width: 470px; height: 840px;
    display: flex; flex-direction: column;
    background: linear-gradient(160deg, var(--screen-top) 0%, var(--screen-mid) 45%, var(--screen-bottom) 100%);
    box-shadow: 0 20px 60px rgba(0,0,0,.35);
  }
  .status-bar {
    height: 28px; background: var(--statusbar);
    display: flex; align-items: center; justify-content: flex-end; gap: 8px;
    padding: 0 12px; font-family: "Roboto", Arial, sans-serif; font-size: 14px;
  }
  .app-bar {
    height: 64px; background: var(--appbar);
    display: flex; align-items: center; justify-content: center;
    font-size: 26px; box-shadow: 0 2px 6px rgba(0,0,0,.2);
  }
  .content { flex: 1; padding: 30px 34px 0; display: flex; flex-direction: column; align-items: center; }
  .welcome { font-size: 25px; align-self: flex-start; }
  .welcome .brand { color: var(--brand); }
  .brand-mark { display: flex; align-items: center; gap: 10px; margin-top: 22px; font-size: 20px; }
  .brand-mark .dot { width: 18px; height: 18px; border-radius: 50%; background: var(--text); }
  .intro { margin-top: 30px; font-size: 17px; line-height: 1.5; }
  .wheel { margin-top: 34px; }
  .spin-button {
    margin-top: auto; margin-bottom: 26px; width: 100%; height: 62px;
    background: var(--button); border: none; color: var(--text);
    font-family: "Roboto", Arial, sans-serif; font-size: 22px;
  }
  .nav-bar {
    height: 64px; background: var(--navbar);
    display: flex; align-items: center; justify-content: space-around;
  }
</style>
</head>
<body>
  <main class="screen">
    <div class="status-bar">
      <svg width="16" height="14" viewBox="0 0 16 14"><path d="M8 13 L0 4 A11 11 0 0 1 16 4 Z" fill="#fff"/></svg>
      <svg width="14" height="14" viewBox="0 0 14 14"><path d="M0 14 L14 0 L14 14 Z" fill="#fff"/></svg>
      <svg width="9" height="15" viewBox="0 0 9 15"><rect x="2.5" y="0" width="4" height="2" fill="#fff"/><rect x="0" y="2" width="9" height="13" rx="1" fill="#fff"/></svg>
      <span>12:06</span>
    </div>
    <header class="app-bar">A Jugar !!!</header>
    <section class="content">
      <h1 class="welcome">Bienvenido a <span class="brand">Cafe Morvana</span></h1>
      <div class="brand-mark"><span class="dot"></span><span>Cafe Morvana</span></div>
      <p class="intro">Hace girar la ruleta y ganate desde ricos capuchinos, tostados, tortas y mucho mas...</p>
      <svg class="wheel" width="220" height="220" viewBox="-110 -110 220 220">
        <circle r="108" fill="var(--wheel-ring)"/>
        <circle r="100" fill="var(--wheel-seg)"/>
        <g stroke="var(--wheel-line)" stroke-width="1.5">
          <line x1="0" y1="-100" x2="0" y2="100"/>
          <line x1="-100" y1="0" x2="100" y2="0"/>
          <line x1="-70.7" y1="-70.7" x2="70.7" y2="70.7"/>
          <line x1="-70.7" y1="70.7" x2="70.7" y2="-70.7"/>
        </g>
        <g fill="#fff">
          <circle cx="26" cy="-63" r="8"/>
          <circle cx="63" cy="-26" r="8"/>
          <circle cx="63" cy="26" r="8"/>
          <circle cx="26" cy="63" r="8"/>
          <circle cx="-26" cy="63" r="8"/>
          <circle cx="-63" cy="26" r="8"/>
          <circle cx="-63" cy="-26" r="8"/>
          <circle cx="-26" cy="-63" r="8"/>
        </g>
        <path d="M0 52 L-12 30 L12 30 Z" fill="var(--pointer)"/>
        <circle r="32" fill="var(--pointer)"/>
        <circle r="26" fill="var(--hub)"/>
      </svg>
      <button class="spin-button">Girar la ruleta ahora !!!</button>
    </section>
    <nav class="nav-bar">
      <svg width="34" height="22" viewBox="0 0 34 22"><path d="M10 2 L2 9 L10 16 M2 9 H24 A8 6 0 0 1 24 21 H14" fill="none" stroke="#c9cdd2" stroke-width="2.5"/></svg>
      <svg width="34" height="22" viewBox="0 0 34 22"><path d="M2 20 L17 3 L32 20 Z" fill="none" stroke="#c9cdd2" stroke-width="2.5"/></svg>
      <svg width="30" height="24" viewBox="0 0 30 24"><rect x="9" y="2" width="19" height="14" fill="none" stroke="#c9cdd2" stroke-width="2.5"/><rect x="2" y="8" width="19" height="14" fill="#050608" stroke="#c9cdd2" stroke-width="2.5"/></svg>
    </nav>
  </main>
</body>
</html>
```